Business card for exciting VC company

Should look simple, crisp, and modern.

Industry/Entity Type

Venture Capital

Contact Information for Business Card

Would like to see at least one design that has our blue on the back with the tagline "Transforming Traditional Industry" and white front with contact details.

Font styles to use
Sans Serif

Requirements
Must have
• Logo

Gregory Tallis
gtallis@brindlewave.vc
Managing Partner
M (628)354-xxxx

```html
<!DOCTYPE html>
<html lang="en">
<head>
<meta charset="utf-8">
<title>Brindlewave Capital – Business Card</title>
<link href="https://fonts.googleapis.com/css2?family=Lato:wght@400;700&display=swap" rel="stylesheet">
<style>
  :root {
    --brand-blue: #4180c4;
    --ink: #111418;
    --paper: #ffffff;
    --backdrop: #2b2c2e;
    --grey-dark: #5d6166;
    --grey-mid: #8e9398;
    --grey-light: #bfc3c7;
    --grey-pale: #dcdee0;
  }
  * { box-sizing: border-box; margin: 0; padding: 0; }
  html, body {
    width: 1200px; height: 1021px; overflow: hidden;
    background: var(--backdrop);
    font-family: "Lato", sans-serif;
  }
  .card {
    position: absolute; left: 280px;
    width: 640px; height: 366px;
    box-shadow: 0 10px 30px rgba(0,0,0,0.45);
  }
  /* Back side */
  .card-back {
    top: 110px;
    background: var(--brand-blue);
  }
  .card-back .wordmark {
    position: absolute; left: 0; right: 0; top: 118px;
    text-align: center; color: var(--ink);
  }
  .wordmark-name {
    display: block;
    font-size: 50px; font-weight: 400; letter-spacing: 4px; line-height: 1;
  }
  .wordmark-sub {
    display: block; margin-top: 8px;
    font-size: 15px; font-weight: 400; letter-spacing: 9px;
  }
  .tagline {
    position: absolute; left: 0; right: 0; bottom: 56px;
    text-align: center; color: var(--paper);
    font-size: 15px; letter-spacing: 1.5px; text-transform: uppercase;
  }
  /* Front side */
  .card-front {
    top: 520px;
    background: linear-gradient(180deg, #ffffff 0%, #f1f2f3 100%);
  }
  .card-front .wordmark {
    position: absolute; left: 40px; top: 130px; width: 250px;
    text-align: center; color: var(--ink);
  }
  .card-front .wordmark-name { font-size: 30px; letter-spacing: 2px; }
  .card-front .wordmark-sub { font-size: 11px; letter-spacing: 7px; margin-top: 6px; }
  .divider {
    position: absolute; left: 328px; top: 86px;
    width: 1.5px; height: 150px; background: var(--brand-blue);
  }
  .contact {
    position: absolute; left: 360px; top: 96px;
    color: var(--ink); font-size: 17px; line-height: 1.3;
  }
  .contact-name { color: var(--brand-blue); font-weight: 700; font-size: 19px; }
  .contact-role { margin-bottom: 12px; }
  .contact-line { display: flex; align-items: center; gap: 7px; }
  .contact-line svg { width: 15px; height: 15px; flex: none; }
  .stripe {
    position: absolute; left: 0; right: 0; bottom: 0; height: 12px;
    display: flex;
  }
  .stripe span { height: 100%; }
  .stripe .s1 { flex: 20; background: var(--brand-blue); }
  .stripe .s2 { flex: 20; background: var(--ink); }
  .stripe .s3 { flex: 14; background: var(--grey-dark); }
  .stripe .s4 { flex: 14; background: var(--grey-mid); }
  .stripe .s5 { flex: 14; background: var(--grey-light); }
  .stripe .s6 { flex: 14; background: var(--grey-pale); }
</style>
</head>
<body>
  <section class="card card-back">
    <div class="wordmark">
      <span class="wordmark-name">BRINDLEWAVE</span>
      <span class="wordmark-sub">CAPITAL</span>
    </div>
    <p class="tagline">Transforming Traditional Industry</p>
  </section>

  <section class="card card-front">
    <div class="wordmark">
      <span class="wordmark-name">BRINDLEWAVE</span>
      <span class="wordmark-sub">CAPITAL</span>
    </div>
    <div class="divider"></div>
    <div class="contact">
      <p class="contact-name">Gregory Tallis</p>
      <p class="contact-role">Managing Partner</p>
      <p class="contact-line">
        <svg viewBox="0 0 16 16" fill="none" stroke="#4180c4" stroke-width="1.3"><rect x="4" y="1.5" width="8" height="13" rx="1.5"/><line x1="7" y1="12" x2="9" y2="12"/></svg>
        (628)354-xxxx
      </p>
      <p class="contact-line">
        <svg viewBox="0 0 16 16" fill="none" stroke="#4180c4" stroke-width="1.3"><rect x="1.5" y="3.5" width="13" height="9"/><polyline points="1.5,3.5 8,9 14.5,3.5"/></svg>
        gtallis@brindlewave.vc
      </p>
      <p class="contact-line">
        <svg viewBox="0 0 16 16" fill="none" stroke="#4180c4" stroke-width="1.2"><circle cx="8" cy="8" r="6.5"/><ellipse cx="8" cy="8" rx="3" ry="6.5"/><line x1="1.5" y1="8" x2="14.5" y2="8"/></svg>
        www.brindlewave.vc
      </p>
    </div>
    <div class="stripe">
      <span class="s1"></span><span class="s2"></span><span class="s3"></span>
      <span class="s4"></span><span class="s5"></span><span class="s6"></span>
    </div>
  </section>
</body>
</html>
```